Steadfast Care - Need Stationary Design

We need a stationary pack for our new Care company based in the uk
Are corporate colours are Pink and purple
Please use attached logo
Target Market(s)
The Care Industry
Industry/Entity Type
It Company
Contact Information for Business Card
Melissa Rowden
Director

```html
<!DOCTYPE html>
<html lang="en">
<head>
<meta charset="utf-8">
<title>Steadfast Care – Stationery Pack</title>
<link href="https://fonts.googleapis.com/css2?family=Raleway:wght@500;600;700&display=swap" rel="stylesheet">
<style>
  :root{
    --backdrop:#d6d5d8;
    --paper:#f4f4f4;
    --purple:#8460b5;
    --pink:#d23eb1;
    --ink:#5a5560;
    --text-font:'Raleway', sans-serif;
  }
  *{box-sizing:border-box;margin:0;padding:0}
  html,body{width:1200px;height:991px;overflow:hidden}
  body{background:var(--backdrop);font-family:var(--text-font);position:relative}
  .piece{position:absolute;background:var(--paper);overflow:hidden}
  .wave{position:absolute;left:0;width:100%;display:block}
  .wave .band-pink{fill:var(--pink)}
  .wave .band-white{fill:var(--paper)}
  .wave .band-purple{fill:var(--purple)}
  .brand{display:flex;align-items:center;gap:6px;color:var(--purple);font-weight:600;white-space:nowrap}
  .brand-dot{border-radius:50%;background:var(--pink);flex:none}
  .contact{font-size:5px;line-height:7px;color:var(--ink);font-weight:500}
  .contact-row{display:flex;align-items:center;gap:3px}
  .contact-row svg{width:5px;height:5px;flex:none}
  .contact .gap{height:4px}

  .letterhead{left:71px;top:104px;width:398px;height:562px}
  .letterhead .brand{position:absolute;left:36px;top:82px;font-size:15px}
  .letterhead .brand-dot{width:10px;height:10px}
  .letterhead .contact{position:absolute;left:286px;top:47px}
  .letterhead .wave{bottom:0;height:26px}

  .folder{left:507px;top:90px;width:433px;height:576px}
  .folder .spine{position:absolute;left:26px;top:0;bottom:0;width:1px;background:rgba(0,0,0,.08)}
  .folder .brand{position:absolute;left:0;right:0;top:134px;justify-content:center;font-size:24px}
  .folder .brand-dot{width:14px;height:14px}
  .folder .wave{top:196px;height:380px}

  .card-front{left:68px;top:696px;width:169px;height:94px}
  .card-front .brand{position:absolute;left:12px;top:52px;font-size:9px;gap:4px}
  .card-front .brand-dot{width:6px;height:6px}
  .card-front .person{position:absolute;left:97px;top:23px}
  .card-front .name{font-size:5px;font-weight:700;color:var(--purple);letter-spacing:.2px}
  .card-front .role{font-size:4px;color:var(--ink);margin-bottom:3px}
  .card-front .contact{font-size:4px;line-height:5.5px}
  .card-front .contact .gap{height:2px}
  .card-front .contact-row svg{width:4px;height:4px}
  .card-front .wave{bottom:0;height:10px}

  .card-back{left:68px;top:810px;width:169px;height:95px;background:var(--purple)}
  .card-back .brand{position:absolute;left:12px;top:58px;font-size:9px;color:#fff;gap:4px}
  .card-back .brand-dot{width:6px;height:6px;background:#fff}

  .compliments{left:266px;top:696px;width:416px;height:209px}
  .compliments .brand{position:absolute;left:16px;top:68px;font-size:13px}
  .compliments .brand-dot{width:9px;height:9px}
  .compliments .address{position:absolute;left:30px;top:175px;font-size:5px;line-height:7px;color:var(--ink)}
  .compliments .wave{bottom:0;height:28px}

  .envelope{left:718px;top:696px;width:416px;height:209px}
  .envelope .flap{position:absolute;left:0;top:0;width:100%;height:59px}
  .envelope .flap-mark{position:absolute;left:202px;top:24px;width:10px;height:10px;border-radius:50%;background:#fff}
  .envelope .web{position:absolute;left:0;right:0;top:182px;text-align:center;font-size:5px;color:var(--ink)}
</style>
</head>
<body>

<svg width="0" height="0" style="position:absolute" aria-hidden="true">
  <defs>
    <symbol id="icon-phone" viewBox="0 0 10 10"><rect width="10" height="10" rx="1.5" fill="#d23eb1"/><path d="M3 2.5c.4 0 .7.9.8 1.4-.2.3-.5.4-.4.7.3.7.8 1.1 1.3 1.3.3.1.4-.2.7-.4.5.1 1.4.4 1.4.8 0 .6-.5 1.2-1.1 1.2C3.9 7.5 2.5 5.8 2.5 3.6c0-.6.2-1.1.5-1.1z" fill="#fff"/></symbol>
    <symbol id="icon-mail" viewBox="0 0 10 10"><rect width="10" height="10" rx="1.5" fill="#d23eb1"/><rect x="2.2" y="3" width="5.6" height="4" fill="none" stroke="#fff" stroke-width=".8"/><path d="M2.2 3l2.8 2.2L7.8 3" fill="none" stroke="#fff" stroke-width=".8"/></symbol>
    <symbol id="icon-web" viewBox="0 0 10 10"><rect width="10" height="10" rx="1.5" fill="#d23eb1"/><circle cx="5" cy="5" r="2.6" fill="none" stroke="#fff" stroke-width=".8"/><path d="M2.4 5h5.2M5 2.4v5.2" stroke="#fff" stroke-width=".6"/></symbol>
  </defs>
</svg>

<!-- Letterhead -->
<section class="piece letterhead">
  <div class="contact">
    <div class="contact-row"><svg><use href="#icon-phone"/></svg>+44 1632 960 418</div>
    <div class="contact-row"><svg><use href="#icon-mail"/></svg>hello@steadfastcare.co.uk</div>
    <div class="contact-row"><svg><use href="#icon-web"/></svg>www.steadfastcare.co.uk</div>
    <div class="gap"></div>
    <div>12 Elm Row, Westfield Park</div>
    <div>Ashby, AB1 2CD</div>
  </div>
  <div class="brand"><span class="brand-dot"></span>Steadfast Care</div>
  <svg class="wave" viewBox="0 0 398 26" preserveAspectRatio="none" aria-hidden="true">
    <path class="band-pink" d="M0 12 C140 4 260 -2 398 18 L398 26 L0 26Z"/>
    <path class="band-white" d="M0 18 C150 8 270 2 398 21 L398 26 L0 26Z"/>
    <path class="band-purple" d="M0 26 L0 24 C150 12 270 6 398 24 L398 26Z"/>
  </svg>
</section>

<!-- Presentation folder -->
<section class="piece folder">
  <div class="brand"><span class="brand-dot"></span>Steadfast Care</div>
  <svg class="wave" viewBox="0 0 433 380" preserveAspectRatio="none" aria-hidden="true">
    <path class="band-pink" d="M0 20 C140 14 260 -2 433 10 L433 380 L0 380Z"/>
    <path class="band-white" d="M0 30 C150 22 270 4 433 18 L433 380 L0 380Z"/>
    <path class="band-purple" d="M0 38 C150 30 280 10 433 26 L433 380 L0 380Z"/>
  </svg>
  <div class="spine"></div>
</section>

<!-- Business card front -->
<section class="piece card-front">
  <div class="brand"><span class="brand-dot"></span>Steadfast Care</div>
  <div class="person">
    <div class="name">DANIEL HARTLEY</div>
    <div class="role">General Manager</div>
    <div class="contact">
      <div class="contact-row"><svg><use href="#icon-phone"/></svg>+44 1632 960 418</div>
      <div class="contact-row"><svg><use href="#icon-mail"/></svg>hello@steadfastcare.co.uk</div>
      <div class="contact-row"><svg><use href="#icon-web"/></svg>www.steadfastcare.co.uk</div>
      <div class="gap"></div>
      <div>12 Elm Row, Westfield Park</div>
      <div>Ashby, AB1 2CD</div>
    </div>
  </div>
  <svg class="wave" viewBox="0 0 169 10" preserveAspectRatio="none" aria-hidden="true">
    <path class="band-pink" d="M0 5 C60 2 110 0 169 6 L169 10 L0 10Z"/>
    <path class="band-white" d="M0 7 C60 4 110 2 169 7.5 L169 10 L0 10Z"/>
    <path class="band-purple" d="M0 10 L0 9 C60 6 110 4 169 9 L169 10Z"/>
  </svg>
</section>

<!-- Business card back -->
<section class="piece card-back">
  <div class="brand"><span class="brand-dot"></span>Steadfast Care</div>
</section>

<!-- Compliments slip -->
<section class="piece compliments">
  <div class="brand"><span class="brand-dot"></span>Steadfast Care</div>
  <div class="address">12 Elm Row, Westfield Park<br>Ashby, AB1 2CD</div>
  <svg class="wave" viewBox="0 0 416 28" preserveAspectRatio="none" aria-hidden="true">
    <path class="band-pink" d="M0 12 C140 4 270 -2 416 18 L416 28 L0 28Z"/>
    <path class="band-white" d="M0 18 C150 8 280 3 416 21 L416 28 L0 28Z"/>
    <path class="band-purple" d="M0 28 L0 24 C150 14 280 8 416 25 L416 28Z"/>
  </svg>
</section>

<!-- Envelope -->
<section class="piece envelope">
  <svg class="flap" viewBox="0 0 416 59" preserveAspectRatio="none" aria-hidden="true">
    <path d="M0 0 H416 L406 54 Q405 59 399 59 H17 Q11 59 10 54Z" fill="var(--purple)"/>
  </svg>
  <span class="flap-mark"></span>
  <div class="web">www.steadfastcare.co.uk</div>
</section>

</body>
</html>
```